Brochure Design Project

We need a brochure to introduce clients who work in our local area to become a VIP clients based on the fact they work in the local area. We have call centers of major companies with 1 km of our hair salon as well as head offices of many big companies some with staff of 400 and Australia second biggest University Carrowby with 1500 international student who live mins away who use our local shops to have lunch as we have many food outlets we have a wide mix of people walking past our salon at lunch time demographic ages from 19yo call center staff to CEO's. I not sure whether to use VIP what are your thoughts and statistics say (overuse). I need your thoughts on how they would qualify to become a VIP i was thinking they only need to show proof they work in one of the offices in our area to become a member I will provide them with a small plastic bar coded tag to identify themselves if they become members you can profile our business from our website www.vessoria.com.au our NEW logo is on our facebook page Vessoria Hair and Make up web logo is the old one I think we should put in our price list which is on our website i was thinking 20% off normal prices subject to change.

Reason: I need more time to organize staff

Target Market(s)

Local traders and local offices we have many call centre staff and big company head offices with in 1 km

Industry/Entity Type

Plastic

Requirements
Must have
• Simplicity not too busy less is more
Nice to have
• A4 Folded
Should not have
• Too much text

```html
<!DOCTYPE html>
<html lang="en">
<head>
<meta charset="utf-8">
<title>Vessoria Price List</title>
<link rel="stylesheet" href="https://fonts.googleapis.com/css2?family=Playball&family=Tinos:wght@400;700&display=swap">
<style>
:root{
  --black:#000;
  --white:#fff;
  --purple:#7a2c91;
  --lavender:#c9b6db;
}
*{margin:0;padding:0;box-sizing:border-box}
html,body{width:1200px;height:1000px;overflow:hidden;background:var(--white)}
body{font-family:"Tinos","Times New Roman",serif;color:var(--white)}
.brochure{position:relative;width:1200px;height:1000px;background:var(--white)}
.sheet{position:absolute;left:0;top:73px;width:1200px;height:852px;background:var(--black);overflow:hidden}
.hero{position:absolute;left:0;top:0;width:1200px;height:480px}
.abs{position:absolute}
.script{font-family:"Playball",cursive;font-weight:400}
.price-tab{left:0;top:182px;width:310px;height:95px;background:var(--purple);border-radius:0 26px 26px 0}
.price-tab h1{position:absolute;left:34px;top:12px;font-size:52px;line-height:1.1;color:var(--white);letter-spacing:1px}
.price-tab .rule{position:absolute;left:30px;top:74px;width:225px;height:2px;background:linear-gradient(90deg,transparent,var(--white),transparent)}
.vip-head{left:785px;top:37px;width:415px;height:68px;background:var(--black);border-radius:14px 0 0 0}
.vip-head h2{position:absolute;left:78px;top:4px;font-size:50px;line-height:1.1;color:var(--white);letter-spacing:1px}
.vip-head .rule{position:absolute;left:58px;top:62px;width:300px;height:2px;background:linear-gradient(90deg,transparent,var(--white),transparent)}
.vip-body{left:785px;top:105px;width:415px;height:125px;background:var(--purple);text-align:center;font-size:16.5px;line-height:20.6px;padding-top:9px}
.sparkles-top{left:755px;top:18px;width:445px;height:110px;z-index:2}
.section-title{font-weight:700;font-size:15.5px;text-transform:uppercase;line-height:20px}
.copy{font-size:16.5px;line-height:20.6px}
.services{left:33px;top:299px;width:318px}
.cuts-panel{left:0;top:427px;width:375px;height:248px;background:var(--purple)}
.cuts-copy{left:33px;top:437px;width:335px}
.colours{left:440px;top:317px;width:318px}
.swatches{left:447px;top:480px;display:flex;gap:15px}
.swatches span{width:38px;height:38px;display:block}
.price-table{position:absolute;border-collapse:collapse;font-size:13.5px;table-layout:fixed}
.price-table td,.price-table th{border:2px solid var(--white);padding:0 6px;text-align:left;font-weight:400;height:22px;line-height:1}
.price-table th{font-size:12.5px;font-weight:700;line-height:1.2}
.price-table th.row-label{font-size:12.5px;white-space:nowrap}
.price-table th.row-label.tight{font-size:11px}
.price-table .note{font-size:12px;height:33px;letter-spacing:-0.3px;white-space:nowrap}
</style>
</head>
<body>
<div class="brochure">
  <div class="sheet">
    <svg class="hero" viewBox="0 0 1200 480">
      <defs>
        <linearGradient id="hairTone" x1="0" y1="0" x2="1" y2="0.35">
          <stop offset="0" stop-color="#4a3a30"/>
          <stop offset="0.3" stop-color="#6e5646"/>
          <stop offset="0.55" stop-color="#3e2e24"/>
          <stop offset="0.8" stop-color="#5d4536"/>
          <stop offset="1" stop-color="#3a2a20"/>
        </linearGradient>
        <linearGradient id="waveLight" x1="0" y1="0" x2="1" y2="0">
          <stop offset="0" stop-color="#9b74b5"/>
          <stop offset="0.5" stop-color="#c3abd8"/>
          <stop offset="1" stop-color="#efe8f5"/>
        </linearGradient>
      </defs>
      <rect x="0" y="0" width="1200" height="360" fill="url(#hairTone)" role="img" aria-label="Close-up photograph of a model with long glossy brown hair sweeping across the top of the spread"/>
      <path d="M0 182 C300 178 480 205 640 250 C810 298 980 335 1200 250 L1200 480 L0 480 Z" fill="var(--purple)"/>
      <path d="M0 228 C300 222 480 252 640 292 C810 336 980 348 1200 282 L1200 480 L0 480 Z" fill="url(#waveLight)"/>
      <path d="M0 236 C300 232 480 262 640 304 C810 350 980 362 1200 300 L1200 480 L0 480 Z" fill="var(--black)"/>
      <g fill="var(--white)">
        <path d="M940 290 Q946 344 1000 350 Q946 356 940 410 Q934 356 870 350 Q934 344 940 290 Z"/>
        <path d="M998 288 Q1001 309 1022 312 Q1001 315 998 336 Q995 315 974 312 Q995 309 998 288 Z"/>
        <path d="M1035 322 Q1039 349 1068 352 Q1039 356 1035 384 Q1031 356 1002 352 Q1031 349 1035 322 Z"/>
      </g>
    </svg>

    <div class="abs price-tab">
      <h1 class="script">Price List</h1>
      <div class="rule"></div>
      <svg class="abs" style="left:240px;top:-12px" width="70" height="70" viewBox="0 0 70 70"><g fill="#fff"><path d="M40 16 Q42 39 64 41 Q42 43 40 66 Q38 43 16 41 Q38 39 40 16 Z"/><path d="M22 0 Q23 12 34 13 Q23 14 22 26 Q21 14 10 13 Q21 12 22 0 Z"/></g></svg>
    </div>

    <div class="abs vip-head">
      <h2 class="script">V.I.P Access</h2>
      <div class="rule"></div>
    </div>
    <div class="abs vip-body">
      VIP Clients will get 15% discount on all services<br>
      (excludes retial purchases) with an additional 5%<br>
      if you visit Monday to Friday before 4:00pm.<br>
      If you work in the local area of Mount Ellery<br>
      (within a 1km range) you could become a VIP today!
    </div>
    <svg class="abs sparkles-top" viewBox="0 0 445 110" aria-hidden="true">
      <g fill="#fff">
        <path d="M36 6 Q39 34 66 38 Q39 42 36 70 Q33 42 6 38 Q33 34 36 6 Z"/>
        <path d="M64 2 Q66 16 80 18 Q66 20 64 34 Q62 20 48 18 Q62 16 64 2 Z"/>
        <path d="M415 70 Q417 82 428 84 Q417 86 415 98 Q413 86 402 84 Q413 82 415 70 Z"/>
      </g>
    </svg>

    <div class="abs services">
      <div class="section-title">Services</div>
      <p class="copy">Maison Aurel Professionnel and Kerevane Paris are the salon’s premium products of choice. A strong partnership Vessoria has shared for many years.</p>
    </div>

    <div class="abs cuts-panel"></div>
    <div class="abs cuts-copy">
      <div class="section-title">Cuts</div>
      <p class="copy">Every consultation gives careful consideration examining face shapes, features and contours. Precise intensive analysis is a reflection of our extensive in-house educational programme.</p>
    </div>

    <table class="price-table" style="left:33px;top:550px;width:325px">
      <colgroup><col style="width:157px"><col style="width:78px"><col style="width:90px"></colgroup>
      <thead><tr style="height:39px"><th class="row-label">CUTTING</th><th>Style Director</th><th>Principal Stylist</th></tr></thead>
      <tbody>
        <tr><td>Ladies’ Style Cut *</td><td>$80.00</td><td>$70.00</td></tr>
        <tr><td>Mens’ Style Cut *</td><td>$55.00</td><td>$45.00</td></tr>
        <tr><td class="note" colspan="3">*Salon Director – from $90.00 (Ladies) and from $65.00 (Men)</td></tr>
      </tbody>
    </table>

    <svg class="abs" style="left:332px;top:680px" width="46" height="46" viewBox="0 0 46 46"><g fill="#fff"><path d="M20 4 Q22 20 38 22 Q22 24 20 40 Q18 24 2 22 Q18 20 20 4 Z"/><path d="M36 22 Q37 29 44 30 Q37 31 36 38 Q35 31 28 30 Q35 29 36 22 Z"/></g></svg>

    <table class="price-table" style="left:33px;top:707px;width:325px">
      <colgroup><col style="width:157px"><col style="width:78px"><col style="width:90px"></colgroup>
      <thead><tr style="height:40px"><th class="row-label">BLOW WAVE/STYLING</th><th>Style Director</th><th>Principal Stylist</th></tr></thead>
      <tbody>
        <tr><td>Short</td><td>$50.00</td><td>$40.00</td></tr>
        <tr><td>Medium</td><td>$60.00</td><td>$50.00</td></tr>
        <tr><td>Long</td><td>$70.00</td><td>$60.00</td></tr>
      </tbody>
    </table>

    <div class="abs colours">
      <div class="section-title">Colours</div>
      <p class="copy">Colour consultations explore a client’s eye colour, skin tone, wants, needs and lifestyle. We offer directional advice, believing it is paramount in stimulating creativity for new ideas or for the refreshment of existing colour.</p>
    </div>

    <div class="abs swatches">
      <span style="background:#ffffff"></span>
      <span style="background:#e5e6e8"></span>
      <span style="background:#cfd0d2"></span>
      <span style="background:#a6a7a9"></span>
      <span style="background:#6d6e70"></span>
      <span style="background:#414042"></span>
    </div>

    <table class="price-table" style="left:437px;top:537px;width:325px">
      <colgroup><col style="width:158px"><col style="width:78px"><col style="width:89px"></colgroup>
      <thead><tr style="height:40px"><th class="row-label">COLOURING</th><th>Technical Director</th><th>Principal Colourist</th></tr></thead>
      <tbody>
        <tr><td>Regrowth</td><td>$80.00</td><td>$65.00</td></tr>
        <tr><td>Short</td><td>$80.00</td><td>$70.00</td></tr>
        <tr><td>Medium</td><td>$90.00</td><td>$80.00</td></tr>
        <tr><td>Long</td><td>$100.00</td><td>$90.00</td></tr>
      </tbody>
    </table>

    <table class="price-table" style="left:437px;top:689px;width:325px">
      <colgroup><col style="width:158px"><col style="width:78px"><col style="width:89px"></colgroup>
      <thead><tr style="height:36px"><th class="row-label tight">NOVA (AMMONIA FREE)</th><th>Technical Director</th><th>Principal Colourist</th></tr></thead>
      <tbody>
        <tr><td>Regrowth</td><td>$85.00</td><td>$75.00</td></tr>
        <tr><td>Short</td><td>$90.00</td><td>$80.00</td></tr>
        <tr><td>Medium</td><td>$100.00</td><td>$95.00</td></tr>
        <tr><td>Long</td><td>$110.00</td><td>$110.00</td></tr>
      </tbody>
    </table>

    <table class="price-table" style="left:840px;top:422px;width:323px">
      <colgroup><col style="width:156px"><col style="width:78px"><col style="width:89px"></colgroup>
      <thead><tr style="height:40px"><th class="row-label">FOILING</th><th>Technical Director</th><th>Principal Colourist</th></tr></thead>
      <tbody>
        <tr><td>½ Head</td><td>$110.00</td><td>$85.00</td></tr>
        <tr><td>Full Head</td><td>$170.00</td><td>$145.00</td></tr>
        <tr><td>Toner</td><td>$15.00</td><td>$10.00</td></tr>
      </tbody>
    </table>

    <table class="price-table" style="left:840px;top:554px;width:323px">
      <colgroup><col style="width:156px"><col style="width:78px"><col style="width:89px"></colgroup>
      <thead><tr style="height:40px"><th class="row-label">FOILS AND COLOUR</th><th>Technical Director</th><th>Principal Colourist</th></tr></thead>
      <tbody>
        <tr><td>Short</td><td>$125.00</td><td>$125.00</td></tr>
        <tr><td>Medium</td><td>$135.00</td><td>$130.00</td></tr>
        <tr><td>Long</td><td>$145.00</td><td>$140.00</td></tr>
        <tr><td>Toner</td><td>$15.00</td><td>$10.00</td></tr>
      </tbody>
    </table>

    <svg class="abs" style="left:814px;top:690px" width="44" height="36" viewBox="0 0 44 36"><g fill="#fff"><path d="M16 4 Q17 16 29 17 Q17 18 16 30 Q15 18 3 17 Q15 16 16 4 Z"/><path d="M32 0 Q33 7 40 8 Q33 9 32 16 Q31 9 24 8 Q31 7 32 0 Z"/></g></svg>

    <table class="price-table" style="left:840px;top:707px;width:323px">
      <colgroup><col style="width:156px"><col style="width:78px"><col style="width:89px"></colgroup>
      <thead><tr style="height:40px"><th class="row-label tight">NOVA (AMMONIA FREE)</th><th>Technical Director</th><th>Principal Colourist</th></tr></thead>
      <tbody>
        <tr><td>Medium</td><td>$160.00</td><td>$145.00</td></tr>
        <tr><td>Long</td><td>$170.00</td><td>$160.00</td></tr>
        <tr><td>Toner</td><td>$15.00</td><td>$10.00</td></tr>
      </tbody>
    </table>
  </div>
</div>
</body>
</html>
```